Painting Contractor Business Card Design

We are looking for a cool, bold, modern, polished, business card design. We are a high-end residential painting contractor. Please incorporate our logo and keep with our green/black color scheme. We are interested in seeing 2-sided and 1-sided options. Thank you very much!

Industry/Entity Type

Business

Contact Information for Business Card

Info for the card:
Owen Talsky
mobile 206-555-0193
email owen@kestrowfinish.net
web www.kestrowfinish.net

```html
<!DOCTYPE html>
<html lang="en">
<head>
<meta charset="utf-8">
<title>Kestrow Finish – Business Card</title>
<link rel="stylesheet" href="https://fonts.googleapis.com/css2?family=Montserrat:wght@300;400;600&family=Open+Sans:wght@400&display=swap">
<style>
  :root {
    --page-bg: #ecebe8;
    --card-white: #ffffff;
    --card-shade: #f1f1f1;
    --ink: #2b2b2b;
    --teal-dark: #0d3f56;
    --teal-mid: #1a5f7a;
    --accent-yellow: #f2c511;
    --accent-green: #6fd07a;
    --contact-text: #f4f7f9;
  }
  * { margin: 0; padding: 0; box-sizing: border-box; }
  html, body {
    width: 1200px; height: 1023px; overflow: hidden;
    background: var(--page-bg);
  }
  .canvas { position: relative; width: 1200px; height: 1023px; }

  .card {
    position: absolute;
    width: 560px; height: 320px;
    border-radius: 4px;
    overflow: hidden;
    box-shadow: 0 10px 28px rgba(0,0,0,.18);
  }

  /* Front */
  .card-front { left: 70px; top: 110px; background: var(--card-white); }
  .front-brand {
    position: absolute; left: 0; top: 0; width: 100%; height: 128px;
    background: linear-gradient(180deg, var(--card-white), var(--card-shade));
    display: flex; align-items: center; padding-left: 44px; gap: 14px;
  }
  .brand-square { width: 22px; height: 22px; background: var(--accent-green); }
  .brand-name {
    font-family: "Montserrat", sans-serif; font-weight: 600;
    font-size: 34px; letter-spacing: 1px; color: var(--ink);
  }
  .front-rule {
    position: absolute; left: 0; top: 128px; width: 100%; height: 6px;
    background: var(--accent-yellow);
  }
  .front-panel {
    position: absolute; left: 0; top: 134px; width: 100%; height: 186px;
    background: linear-gradient(160deg, var(--teal-mid), var(--teal-dark));
    display: flex; align-items: center;
  }
  .holder-name {
    width: 230px; text-align: center;
    font-family: "Montserrat", sans-serif; font-weight: 300;
    font-size: 27px; color: var(--accent-green);
  }
  .panel-divider { width: 1px; height: 104px; background: rgba(255,255,255,.55); }
  .contact-list {
    list-style: none; padding-left: 26px;
    font-family: "Open Sans", sans-serif; font-size: 17px; color: var(--contact-text);
  }
  .contact-list li { display: flex; align-items: center; gap: 10px; line-height: 30px; }
  .contact-list svg { width: 15px; height: 15px; flex: none; }

  /* Back */
  .card-back {
    left: 570px; top: 590px;
    background: linear-gradient(135deg, var(--card-white), var(--card-shade));
    display: flex; align-items: center; justify-content: center; gap: 16px;
  }
  .card-back .brand-name { font-size: 38px; }
  .card-back .brand-square { width: 26px; height: 26px; }
</style>
</head>
<body>
<main class="canvas">
  <section class="card card-front" aria-label="Business card front">
    <div class="front-brand">
      <span class="brand-square"></span>
      <span class="brand-name">KESTROW FINISH</span>
    </div>
    <div class="front-rule"></div>
    <div class="front-panel">
      <p class="holder-name">Owen Talsky</p>
      <span class="panel-divider"></span>
      <ul class="contact-list">
        <li>
          <svg viewBox="0 0 16 16" aria-hidden="true"><path fill="#f2c511" d="M3 1h3l1.5 3.5-2 1.3a9 9 0 0 0 4.7 4.7l1.3-2L15 10v3a2 2 0 0 1-2 2A12 12 0 0 1 1 3a2 2 0 0 1 2-2z"/></svg>
          206-555-0193
        </li>
        <li>
          <svg viewBox="0 0 16 16" aria-hidden="true"><rect x="1" y="3" width="14" height="10" rx="1" fill="#f2c511"/><path d="M1.5 3.5 8 9l6.5-5.5" fill="none" stroke="#0d3f56" stroke-width="1.3"/></svg>
          owen@kestrowfinish.net
        </li>
        <li>
          <svg viewBox="0 0 16 16" aria-hidden="true"><circle cx="8" cy="8" r="7" fill="#f2c511"/><path d="M1 8h14M8 1c-3 3.5-3 10.5 0 14M8 1c3 3.5 3 10.5 0 14" fill="none" stroke="#0d3f56" stroke-width="1"/></svg>
          www.kestrowfinish.net
        </li>
      </ul>
    </div>
  </section>

  <section class="card card-back" aria-label="Business card back">
    <span class="brand-square"></span>
    <span class="brand-name">KESTROW FINISH</span>
  </section>
</main>
</body>
</html>
```